Yard sign

Looking for a yard sign. <br/>Something simple, name, number. <br/>Large text, readable from 50 feet away. <br/><br/>18 x 24 inches.

Target Market(s)

Potential homeowners thinking about going solar.

Colors

Designer to choose colors to be used in the design.

Requirements
Must have
• "WE'VE GONE SOLAR!"
Nice to have
• We are a solar company, we would like a design that compliments the homeowners decision that they went solar and encourages others to do the same.

```html
<!DOCTYPE html>
<html lang="en">
<head>
<meta charset="utf-8">
<title>We've Gone Solar! – Yard Sign</title>
<link rel="stylesheet" href="https://fonts.googleapis.com/css2?family=Bowlby+One&display=swap">
<style>
  :root {
    --paper: #f3f8f6;
    --frame-gold: #fcc316;
    --sky-deep: #07090d;
    --sky-blue: #0b2547;
    --sun-core: #fdc813;
    --sun-edge: #fd7e0f;
    --outline: #111214;
    --contact-white: #f3f8f6;
  }
  html, body {
    margin: 0;
    padding: 0;
    width: 1200px;
    height: 900px;
    overflow: hidden;
    background: var(--paper);
  }
  .yard-sign {
    position: relative;
    width: 1200px;
    height: 900px;
  }
  .sign-frame {
    position: absolute;
    inset: 11px;
    background: var(--frame-gold);
  }
  .sign-panel {
    position: absolute;
    inset: 13px;
    overflow: hidden;
  }
  .night-sky {
    position: absolute;
    inset: 0;
    background:
      radial-gradient(ellipse 45% 40% at 18% 25%, rgba(20, 60, 100, .55), transparent 70%),
      radial-gradient(ellipse 45% 45% at 95% 65%, rgba(15, 45, 110, .7), transparent 70%),
      var(--sky-deep);
  }
  .sign-art {
    position: absolute;
    inset: 0;
    width: 100%;
    height: 100%;
  }
  .headline {
    font-family: "Bowlby One", "Arial Black", sans-serif;
    fill: url(#sun-glow);
    stroke: var(--outline);
    stroke-width: 10px;
    stroke-linejoin: round;
    paint-order: stroke fill;
  }
  .headline--top { font-size: 150px; }
  .headline--main { font-size: 300px; stroke-width: 14px; }
  .brand-name {
    font-family: "Bowlby One", "Arial Black", sans-serif;
    font-size: 64px;
    fill: var(--sun-edge);
  }
  .brand-dot { fill: var(--frame-gold); }
  .contact-line {
    font-family: "Bowlby One", "Arial Black", sans-serif;
    font-size: 46px;
    fill: var(--contact-white);
    letter-spacing: 2px;
  }
</style>
</head>
<body>
  <main class="yard-sign">
    <div class="sign-frame">
      <div class="sign-panel">
        <div class="night-sky" role="img" aria-label="Night sky scattered with small stars"></div>
        <svg class="sign-art" viewBox="0 0 1152 852" xmlns="http://www.w3.org/2000/svg">
          <defs>
            <radialGradient id="sun-glow" cx="50%" cy="55%" r="60%">
              <stop offset="0%" stop-color="var(--sun-core)"/>
              <stop offset="45%" stop-color="var(--sun-core)"/>
              <stop offset="100%" stop-color="var(--sun-edge)"/>
            </radialGradient>
            <path id="headline-arc" d="M 130 250 Q 576 -10 1022 250"/>
          </defs>

          <text class="headline headline--top">
            <textPath href="#headline-arc" startOffset="50%" text-anchor="middle">WE’VE GONE</textPath>
          </text>

          <text class="headline headline--main" x="576" y="540" text-anchor="middle"
                textLength="1060" lengthAdjust="spacingAndGlyphs">SOLAR!</text>

          <g class="brand">
            <circle class="brand-dot" cx="400" cy="685" r="38"/>
            <text class="brand-name" x="455" y="708">BRIGHTLINE SOLAR</text>
          </g>

          <text class="contact-line" x="576" y="823" text-anchor="middle"
                textLength="1100" lengthAdjust="spacingAndGlyphs">(555)-201-4477 • www.brightlinesolar.com</text>
        </svg>
      </div>
    </div>
  </main>
</body>
</html>
```